Business card design needed

would like the title calloway estate works to itself be a logo which would also be suitable to use on my van signwriting so needs to be bold and stand out (easily read from a distance)
Target Market(s)
real estate agents, property owners/investors,insurance assessors,
Industry/Entity Type
Business
Contact Information for Business Card
calloway estate works
for all your property maintenance and repair needs
-domestic and commercial -rental properties
-insurance repairs -project managment
fully insured/white card
experieced and reliable
ph. ned calloway 0418526093 email nedster4731@webhollow.net.au
on reverse side of card i would like a list of sevices available
plaster repairs
painting
welding reairs and fabrication
concreting
fencing
minor renovations
pressure cleaning
graffitti removal
rubbish removal
fire restorations
floods
and more no job too big or small
Logo Text
Logo styles of interest
Wordmark Logo

```html
<!DOCTYPE html>
<html lang="en">
<head>
<meta charset="utf-8">
<title>Calloway Estate Works – Business Card</title>
<link rel="stylesheet" href="https://fonts.googleapis.com/css2?family=Open+Sans:ital,wght@0,400;0,600;0,700;0,800;1,400;1,600;1,700&display=swap">
<style>
  :root {
    --bg: #ece9e6;
    --card-white: #ffffff;
    --red: #cf1820;
    --red-dark: #8c0a10;
    --ink: #141414;
    --on-red: #ffffff;
    --accent: #f6a21c;
    --rule: #2a0406;
  }
  * { margin: 0; padding: 0; box-sizing: border-box; }
  html, body {
    width: 1200px; height: 868px; overflow: hidden;
    background: var(--bg);
    font-family: "Open Sans", Arial, sans-serif;
  }
  .canvas { position: relative; width: 1200px; height: 868px; }

  .card {
    position: absolute; left: 280px;
    width: 640px; height: 366px;
    border-radius: 14px; overflow: hidden;
    background: var(--card-white);
    box-shadow: 0 6px 18px rgba(0,0,0,0.18);
  }

  /* Reverse: services + contact */
  .card-reverse { top: 40px; display: flex; }
  .services-panel {
    width: 46%; height: 100%;
    background: linear-gradient(135deg, var(--red) 0%, var(--red-dark) 100%);
    color: var(--on-red);
    padding: 58px 0 0 48px;
    font-style: italic;
  }
  .services-list { list-style: none; }
  .services-list li {
    display: flex; align-items: center; gap: 10px;
    font-size: 15px; line-height: 22px;
  }
  .tick { width: 13px; height: 13px; flex: none; }
  .services-closing {
    margin-top: 22px; text-align: center; padding-right: 40px;
    color: var(--accent); font-weight: 700; font-size: 15px; line-height: 20px;
  }
  .contact-side { flex: 1; padding: 40px 0 0 34px; }
  .wordmark { color: var(--red); font-weight: 800; text-transform: uppercase; line-height: 1.05; }
  .wordmark-small .name-main { font-size: 40px; letter-spacing: 2px; display: block; }
  .wordmark-small .name-sub { font-size: 24px; letter-spacing: 1px; display: block; }
  .person { margin-top: 46px; }
  .person-name { color: var(--red); font-weight: 700; font-size: 22px; }
  .person-role { color: var(--ink); font-weight: 700; font-size: 13px; margin-top: 2px; }
  .person-contact { margin-top: 30px; color: var(--ink); font-size: 14px; line-height: 20px; }

  /* Front */
  .card-front { top: 462px; display: flex; flex-direction: column; }
  .front-logo-area {
    height: 58%; display: flex; flex-direction: column;
    align-items: center; justify-content: center; padding-top: 16px;
  }
  .wordmark-large .name-main { font-size: 60px; letter-spacing: 4px; display: block; text-align: center; }
  .wordmark-large .name-sub { font-size: 36px; letter-spacing: 1px; display: block; text-align: center; }
  .front-band {
    flex: 1;
    background: linear-gradient(180deg, var(--red) 0%, var(--red-dark) 100%);
    color: var(--on-red); text-align: center; padding-top: 16px;
  }
  .tagline { font-style: italic; font-weight: 700; font-size: 21px; }
  .band-rule { width: 400px; height: 2px; background: var(--rule); margin: 12px auto 16px; }
  .features { font-size: 14.5px; line-height: 20px; }
  .features .sep { margin: 0 16px; }
</style>
</head>
<body>
<main class="canvas">

  <section class="card card-reverse" aria-label="Card reverse: services and contact">
    <div class="services-panel">
      <ul class="services-list">
        <li><svg class="tick" viewBox="0 0 13 13"><rect x="0.5" y="0.5" width="12" height="12" fill="#fff"/><path d="M3 6.5 L5.5 9 L10.5 3" fill="none" stroke="#8c0a10" stroke-width="2"/></svg>painting</li>
        <li><svg class="tick" viewBox="0 0 13 13"><rect x="0.5" y="0.5" width="12" height="12" fill="#fff"/><path d="M3 6.5 L5.5 9 L10.5 3" fill="none" stroke="#8c0a10" stroke-width="2"/></svg>welding</li>
        <li><svg class="tick" viewBox="0 0 13 13"><rect x="0.5" y="0.5" width="12" height="12" fill="#fff"/><path d="M3 6.5 L5.5 9 L10.5 3" fill="none" stroke="#8c0a10" stroke-width="2"/></svg>reairs and fabrication</li>
        <li><svg class="tick" viewBox="0 0 13 13"><rect x="0.5" y="0.5" width="12" height="12" fill="#fff"/><path d="M3 6.5 L5.5 9 L10.5 3" fill="none" stroke="#8c0a10" stroke-width="2"/></svg>concreting</li>
        <li><svg class="tick" viewBox="0 0 13 13"><rect x="0.5" y="0.5" width="12" height="12" fill="#fff"/><path d="M3 6.5 L5.5 9 L10.5 3" fill="none" stroke="#8c0a10" stroke-width="2"/></svg>fencing</li>
        <li><svg class="tick" viewBox="0 0 13 13"><rect x="0.5" y="0.5" width="12" height="12" fill="#fff"/><path d="M3 6.5 L5.5 9 L10.5 3" fill="none" stroke="#8c0a10" stroke-width="2"/></svg>minor renovations</li>
        <li><svg class="tick" viewBox="0 0 13 13"><rect x="0.5" y="0.5" width="12" height="12" fill="#fff"/><path d="M3 6.5 L5.5 9 L10.5 3" fill="none" stroke="#8c0a10" stroke-width="2"/></svg>pressure cleaning</li>
        <li><svg class="tick" viewBox="0 0 13 13"><rect x="0.5" y="0.5" width="12" height="12" fill="#fff"/><path d="M3 6.5 L5.5 9 L10.5 3" fill="none" stroke="#8c0a10" stroke-width="2"/></svg>graffitti removal</li>
        <li><svg class="tick" viewBox="0 0 13 13"><rect x="0.5" y="0.5" width="12" height="12" fill="#fff"/><path d="M3 6.5 L5.5 9 L10.5 3" fill="none" stroke="#8c0a10" stroke-width="2"/></svg>rubbish removal</li>
        <li><svg class="tick" viewBox="0 0 13 13"><rect x="0.5" y="0.5" width="12" height="12" fill="#fff"/><path d="M3 6.5 L5.5 9 L10.5 3" fill="none" stroke="#8c0a10" stroke-width="2"/></svg>fire restorations floods</li>
      </ul>
      <p class="services-closing">and more,<br>no job too big or small</p>
    </div>
    <div class="contact-side">
      <h2 class="wordmark wordmark-small">
        <span class="name-main">Calloway</span>
        <span class="name-sub">Estate Works</span>
      </h2>
      <div class="person">
        <p class="person-name">Ned Calloway</p>
        <p class="person-role">SEO</p>
        <p class="person-contact">0418526093<br>nedster4731@webhollow.net.au</p>
      </div>
    </div>
  </section>

  <section class="card card-front" aria-label="Card front">
    <div class="front-logo-area">
      <h1 class="wordmark wordmark-large">
        <span class="name-main">Calloway</span>
        <span class="name-sub">Estate Works</span>
      </h1>
    </div>
    <div class="front-band">
      <p class="tagline">for all your property maintenance and repair needs</p>
      <div class="band-rule"></div>
      <p class="features">domestic and commercial<span class="sep">|</span>rental properties<span class="sep">|</span>insurance repairs</p>
      <p class="features">project managment fully insured<span class="sep">|</span>experieced and reliable</p>
    </div>
  </section>

</main>
</body>
</html>
```